Velkano Holdings Ltd - An invesmtent & trading company needs a web design

We need a web design for our company based in Cyprus. The company was founded in 2009. We have continuously grown and now invest & trade all over the world.

Velkano Holdings ltd. specializes in the buying and selling of crude oil, precious metals and the investment in properties.

We know that trust is of the utmost importance when it comes to business and the design should communicate this to prospective business partners. Find attached the company logo. The colour scheme for the website should use similar colours and ideally incorporate the logo in some shape or form as well.

Target Market(s)

Oil Traders, Metall Traders, Property Investments

Industry/Entity Type

Trade

Coding

Coded - Design and coding required

Number of Pages Required

4 page

Font styles to use
Sans Serif

Requirements
Must have
• Mainpage,
• About Us
• Partners
• Legal Notice

```html
<!DOCTYPE html>
<html lang="en">
<head>
<meta charset="utf-8">
<title>Velkano Holdings Ltd</title>
<link href="https://fonts.googleapis.com/css2?family=Raleway:wght@400;600;700;800&family=Open+Sans:wght@400;600&display=swap" rel="stylesheet">
<style>
:root{
  --blue:#19a6da;
  --blue-dark:#1186b4;
  --navy:#1c3d72;
  --ink:#333a40;
  --muted:#7a8086;
  --light:#f1f2f3;
  --line:#d9dcde;
  --footer:#2a2b2d;
  --white:#ffffff;
}
*{box-sizing:border-box;margin:0;padding:0}
html,body{width:788px;height:1200px;overflow:hidden}
body{font-family:"Open Sans",Arial,sans-serif;color:var(--ink);background:var(--white);position:relative}
.site-header{position:absolute;left:0;top:0;width:788px;height:112px;z-index:3}
.header-shape{position:absolute;left:0;top:0}
.topbar{position:absolute;left:26px;right:26px;top:8px;display:flex;justify-content:space-between;align-items:center;font-size:9px;color:var(--muted)}
.topbar .phone{display:flex;align-items:center;gap:5px}
.social{display:flex;gap:4px}
.social span{width:13px;height:13px;background:var(--blue);display:block;border-radius:2px}
.brand{position:absolute;left:26px;top:30px;display:flex;align-items:center;gap:8px}
.brand-mark{width:30px;height:30px;background:var(--navy)}
.brand-name{font-family:"Raleway",sans-serif;font-weight:800;font-size:17px;line-height:16px;color:var(--navy);letter-spacing:.5px}
.main-nav{position:absolute;right:26px;top:52px;display:flex}
.main-nav a{font-family:"Raleway",sans-serif;font-size:9px;font-weight:600;color:var(--ink);text-decoration:none;padding:6px 12px;text-transform:uppercase}
.main-nav a.active{color:var(--blue);border-bottom:2px solid var(--blue)}
.hero{position:absolute;left:0;top:60px;width:788px;height:440px}
.hero-photo{position:absolute;inset:0;background:linear-gradient(100deg,#3a3f44 0%,#5d6166 45%,#8c8f92 75%,#6b6e71 100%)}
.hero-shade{position:absolute;inset:0;background:rgba(20,24,28,.45)}
.hero-content{position:absolute;left:0;right:0;top:146px;text-align:center;color:var(--white)}
.hero-title{font-family:"Raleway",sans-serif;font-weight:600;font-size:23px;letter-spacing:.5px;display:inline-block;padding:10px 0;border-top:1px solid rgba(255,255,255,.6);border-bottom:1px solid rgba(255,255,255,.6)}
.hero-text{width:440px;margin:12px auto 0;font-size:9px;line-height:14px;color:#e3e5e7}
.btn{display:inline-block;font-family:"Raleway",sans-serif;font-size:8px;font-weight:700;text-transform:uppercase;padding:7px 16px;background:var(--blue);color:var(--white);text-decoration:none}
.btn-outline{background:var(--white);color:var(--blue);border:1px solid var(--blue)}
.hero .btn{margin-top:20px}
.dots{position:absolute;left:0;right:0;top:325px;display:flex;justify-content:center;gap:6px}
.dots span{width:8px;height:8px;border-radius:50%;border:1px solid var(--white)}
.dots span.on{background:var(--white)}
.welcome{position:absolute;left:0;top:500px;width:788px;height:178px;text-align:center}
.welcome h1{margin-top:22px;font-family:"Raleway",sans-serif;font-weight:700;font-size:19px;color:var(--ink);text-transform:uppercase}
.welcome h1 em{font-style:normal;color:var(--blue);font-weight:600}
.welcome p{width:500px;margin:12px auto 0;font-size:8.5px;line-height:13px;color:var(--muted)}
.welcome .btn{margin-top:18px}
.services{position:absolute;left:0;top:678px;width:788px;height:244px;background:var(--light);display:flex;justify-content:space-between;padding:14px 24px 0}
.service{width:226px;height:206px;text-align:center;padding-top:20px}
.service.featured{background:var(--white);border:1px solid var(--line)}
.service-icon{width:50px;height:50px;margin:0 auto;background:var(--blue)}
.service h3{margin-top:14px;font-family:"Raleway",sans-serif;font-weight:700;font-size:11px;color:var(--blue);text-transform:uppercase}
.service p{width:180px;margin:8px auto 0;font-size:8px;line-height:12px;color:var(--muted)}
.service .btn{margin-top:14px}
.partners{position:absolute;left:0;top:922px;width:788px;height:90px;display:flex;align-items:center;justify-content:center;gap:10px}
.partners .arrow{width:14px;height:30px;display:flex;align-items:center;justify-content:center}
.partner{width:122px;height:48px;border:1px solid var(--line);display:flex;align-items:center;justify-content:center}
.partner span{display:block;height:16px;background:#c9cdd1;border-radius:3px}
.site-footer{position:absolute;left:0;top:1016px;width:788px;height:128px;background:var(--footer);color:#e4e4e4;font-size:12px}
.contact{position:absolute;display:flex;align-items:center;gap:14px}
.copyright{position:absolute;left:0;top:1144px;width:788px;height:56px;background:var(--blue);color:var(--white);font-size:7.5px;display:flex;align-items:center;justify-content:center}
</style>
</head>
<body>

<header class="site-header">
  <svg class="header-shape" width="788" height="112" viewBox="0 0 788 112" aria-hidden="true">
    <path d="M0 0H788V86C600 112 420 72 250 92C150 104 60 98 0 90Z" fill="#ffffff"/>
  </svg>
  <div class="topbar">
    <div class="phone">
      <svg width="9" height="9" viewBox="0 0 24 24"><path d="M6.6 10.8a15 15 0 0 0 6.6 6.6l2.2-2.2a1 1 0 0 1 1-.25 11.4 11.4 0 0 0 3.6.57 1 1 0 0 1 1 1V20a1 1 0 0 1-1 1A17 17 0 0 1 3 4a1 1 0 0 1 1-1h3.5a1 1 0 0 1 1 1c0 1.25.2 2.45.57 3.57a1 1 0 0 1-.25 1Z" fill="#19a6da"/></svg>
      0800-123-4567
    </div>
    <div class="social"><span></span><span></span><span></span></div>
  </div>
  <div class="brand">
    <div class="brand-mark"></div>
    <div class="brand-name">VELKANO<br>HOLDINGS LTD</div>
  </div>
  <nav class="main-nav">
    <a href="#" class="active">Home</a>
    <a href="#">About Us</a>
    <a href="#">Partners</a>
    <a href="#">Legal Notice</a>
  </nav>
</header>

<section class="hero">
  <div class="hero-photo" role="img" aria-label="Photo of business people working at a laptop"></div>
  <div class="hero-shade"></div>
  <div class="hero-content">
    <h2 class="hero-title">LOREM IPSUM DOLOR SIT AMET, CONSECTETUR</h2>
    <p class="hero-text">Lorem ipsum dolor sit amet, consectetur adipiscing elit, sed do eiusmod tempor incididunt ut labore et dolore magna aliqua. Ut enim ad minim veniam, quis nostrud exercitation ullamco laboris.</p>
    <a href="#" class="btn">Read more</a>
  </div>
  <div class="dots"><span></span><span class="on"></span><span></span></div>
</section>

<section class="welcome">
  <h1>Welcome to Velkano <em>Holdings Ltd</em></h1>
  <p>Lorem ipsum dolor sit amet, consectetur adipiscing elit, sed do eiusmod tempor incididunt ut labore et dolore magna aliqua. Ut enim ad minim veniam, quis nostrud exercitation ullamco laboris nisi ut aliquip ex ea commodo consequat. Duis aute irure dolor in reprehenderit in voluptate velit esse cillum dolore eu fugiat nulla pariatur. Excepteur sint occaecat cupidatat non proident, sunt in culpa qui officia deserunt mollit anim id est laborum.</p>
  <a href="#" class="btn">Read more</a>
</section>

<section class="services">
  <article class="service featured">
    <div class="service-icon" aria-hidden="true"></div>
    <h3>Lorem ipsum dolor</h3>
    <p>Lorem ipsum dolor sit amet, consectetur adipiscing elit, sed do eiusmod tempor incididunt ut labore et dolore magna aliqua.</p>
    <a href="#" class="btn">Read more</a>
  </article>
  <article class="service">
    <div class="service-icon" aria-hidden="true"></div>
    <h3>Lorem ipsum dolor</h3>
    <p>Lorem ipsum dolor sit amet, consectetur adipiscing elit, sed do eiusmod tempor incididunt ut labore et dolore magna aliqua.</p>
    <a href="#" class="btn btn-outline">Read more</a>
  </article>
  <article class="service">
    <div class="service-icon" aria-hidden="true"></div>
    <h3>Lorem ipsum dolor</h3>
    <p>Lorem ipsum dolor sit amet, consectetur adipiscing elit, sed do eiusmod tempor incididunt ut labore et dolore magna aliqua.</p>
    <a href="#" class="btn btn-outline">Read more</a>
  </article>
</section>

<section class="partners" aria-label="Partners">
  <div class="arrow"><svg width="8" height="14" viewBox="0 0 8 14"><path d="M7 1L1 7L7 13" fill="none" stroke="#9aa0a5" stroke-width="1.5"/></svg></div>
  <div class="partner"><span style="width:70px"></span></div>
  <div class="partner"><span style="width:64px"></span></div>
  <div class="partner"><span style="width:58px"></span></div>
  <div class="partner"><span style="width:66px"></span></div>
  <div class="partner"><span style="width:44px;height:24px"></span></div>
  <div class="arrow"><svg width="8" height="14" viewBox="0 0 8 14"><path d="M1 1L7 7L1 13" fill="none" stroke="#9aa0a5" stroke-width="1.5"/></svg></div>
</section>

<footer class="site-footer">
  <div class="contact" style="left:62px;top:30px">
    <svg width="16" height="16" viewBox="0 0 24 24"><path d="M6.6 10.8a15 15 0 0 0 6.6 6.6l2.2-2.2a1 1 0 0 1 1-.25 11.4 11.4 0 0 0 3.6.57 1 1 0 0 1 1 1V20a1 1 0 0 1-1 1A17 17 0 0 1 3 4a1 1 0 0 1 1-1h3.5a1 1 0 0 1 1 1c0 1.25.2 2.45.57 3.57a1 1 0 0 1-.25 1Z" fill="#e4e4e4"/></svg>
    123.456.7890
  </div>
  <div class="contact" style="left:276px;top:30px">
    <svg width="16" height="16" viewBox="0 0 24 24"><path d="M4 8H20V19H4Z M7 3H17V8H7Z" fill="#e4e4e4"/><path d="M8 12H16M8 15H13" stroke="#2a2b2d" stroke-width="1.5"/></svg>
    123.456.7890
  </div>
  <div class="contact" style="left:492px;top:30px">
    <svg width="16" height="12" viewBox="0 0 24 18"><path d="M1 1H23V17H1Z" fill="none" stroke="#e4e4e4" stroke-width="2"/><path d="M1 1L12 10L23 1" fill="none" stroke="#e4e4e4" stroke-width="2"/></svg>
    info@velkanoholdings.com
  </div>
  <div class="contact" style="left:62px;top:80px">
    <svg width="14" height="18" viewBox="0 0 14 20"><path d="M7 0A7 7 0 0 0 0 7C0 12 7 20 7 20S14 12 14 7A7 7 0 0 0 7 0Z" fill="#e4e4e4"/><circle cx="7" cy="7" r="2.5" fill="#2a2b2d"/></svg>
    Address Line1, Address line2, 12345, Country
  </div>
</footer>

<div class="copyright">All Rights Reserved. Copyright 2015 Velkano Holdings Ltd.</div>

</body>
</html>
```